White Paper and One-Page Advertisement for TELVAMORE-QX

I need both documents to be better formatted and designed so they look professional, not something someone with mediocre word skills put together. They will go out to 1000s of industry professionals, and they need to look sharp. I need them to have my company's color palate logo, and branding on it similar to how it is now, but better. Please do not change any of the written content, but it can be arranged in any other format you think is better. Smart art and things i've already used can be omitted in favor of better designs. The developer is free to use their creativity. White paper should not be longer than the three pages unless necessary.

Target Market(s)

Life Sciences supply chain professionals

Colors
33b8a4
0592cd
9bcb3c
fbee3e
3277b5

Requirements
Must have
• Must be professional looking and not look like something done in word. Please use the color palate as seen on the documents.
Should not have
• Any changes to the written content.

```html
<!DOCTYPE html>
<html lang="en">
<head>
<meta charset="utf-8">
<title>TELVAMORE-QX – One-Page Advertisement</title>
<link href="https://fonts.googleapis.com/css2?family=Poppins:wght@400;500;600;700&family=Exo+2:ital,wght@1,800&family=Roboto+Condensed:wght@700&display=swap" rel="stylesheet">
<style>
  :root{
    --teal-dark:#1a7f70;
    --teal:#2a9a86;
    --green:#8dc63f;
    --green-deep:#7ab41d;
    --ink:#222;
    --panel:#f0f0f0;
    --page:#ffffff;
    --backdrop:#e6e6e6;
  }
  *{margin:0;padding:0;box-sizing:border-box}
  html,body{width:1200px;height:1200px;overflow:hidden;background:var(--backdrop)}
  body{font-family:'Poppins',sans-serif;color:var(--ink)}
  .flyer{position:absolute;left:200px;top:34px;width:800px;height:1132px;background:var(--page);overflow:hidden}
  .abs{position:absolute}
  .brand-panel{left:501px;top:0;width:299px;height:163px;background:var(--panel);display:flex;align-items:center;justify-content:center;gap:10px}
  .brand-dot{width:16px;height:16px;border-radius:50%;background:var(--teal-dark)}
  .brand-name{font-family:'Poppins',sans-serif;font-weight:700;font-size:25px;color:var(--teal-dark);letter-spacing:.5px}
  .section-title{font-family:'Exo 2',sans-serif;font-style:italic;font-weight:800;font-size:24px;letter-spacing:-.5px}
  .section-title .lead{color:var(--teal-dark)}
  .section-title .rest{color:var(--green)}
  .bullets{list-style:none;font-size:14.5px;line-height:18px}
  .bullets li{position:relative;padding-left:20px}
  .bullets li::before{content:"";position:absolute;left:1px;top:5px;width:10px;height:10px;border-radius:50%;background:var(--teal-dark)}
  .process{left:58px;top:199px;width:700px;height:162px}
  .step-label{font-family:'Roboto Condensed',sans-serif;font-weight:700;font-size:13.5px;fill:#fff;text-anchor:middle}
  .benefits-tab{left:0;top:478px;width:250px;height:50px}
  .benefits-tab span{position:absolute;left:55px;top:9px;font-family:'Exo 2',sans-serif;font-style:italic;font-weight:800;font-size:24px;color:#fff}
  .benefits-band{left:0;top:527px;width:800px;height:162px;background:var(--green)}
  .benefit{position:absolute;color:#fff;font-size:15px;line-height:15px;font-weight:500}
  .benefit svg{position:absolute;left:-28px;top:-1px}
  .photo{left:0;top:804px;width:525px;height:328px;background:linear-gradient(135deg,#6b3f26 0%,#a3683c 35%,#2f5d63 70%,#1f3f44 100%)}
  .contact{left:545px;width:240px}
  .contact .label{color:var(--teal-dark);font-weight:700;font-size:16px;line-height:20px}
  .contact .value{font-weight:700;font-size:16px;line-height:20px;color:var(--ink)}
  .about{left:545px;top:995px;width:208px;font-size:11.5px;line-height:15.5px;text-align:justify}
  .about p+p{margin-top:11px}
</style>
</head>
<body>
<div class="flyer">

  <div class="abs brand-panel"><span class="brand-dot"></span><span class="brand-name">TELVAMORE-QX</span></div>

  <h2 class="abs section-title" style="left:50px;top:36px"><span class="lead">OUR</span> <span class="rest">PLATFORM</span></h2>
  <ul class="abs bullets" style="left:50px;top:90px;width:440px">
    <li>A multi-vendor marketplace for the life science community to transact pre-market and after-market materials and equipment</li>
    <li style="margin-top:18px">Researchers, manufactures, and original suppliers can create an account to buy, sell, or donate materials</li>
  </ul>

  <svg class="abs process" viewBox="0 0 700 162" aria-label="Platform process">
    <g stroke="#fff" stroke-width="4" stroke-linejoin="miter">
      <polygon fill="var(--green)" points="0,25 135,25 135,0 205,81 135,162 135,137 0,137 40,81"/>
      <polygon fill="var(--green-deep)" points="166,25 300,25 300,0 370,81 300,162 300,137 166,137 206,81"/>
      <polygon fill="var(--teal)" points="332,25 466,25 466,0 536,81 466,162 466,137 332,137 372,81"/>
      <polygon fill="var(--teal-dark)" points="498,25 632,25 632,0 696,81 632,162 632,137 498,137 538,81"/>
    </g>
    <!-- shield -->
    <path d="M103 36 l17 6 v12 c0 10-8 16-17 20 c-9-4-17-10-17-20 v-12z" fill="#fff"/>
    <path d="M96 55 l5 5 l9-10" stroke="var(--green)" stroke-width="3" fill="none"/>
    <text class="step-label" x="103" y="106">Authentication and</text>
    <text class="step-label" x="103" y="123">terms of quality</text>
    <!-- gears -->
    <circle cx="265" cy="46" r="7" fill="none" stroke="#fff" stroke-width="4" stroke-dasharray="3 2"/>
    <circle cx="279" cy="60" r="9" fill="none" stroke="#fff" stroke-width="5" stroke-dasharray="3 2"/>
    <text class="step-label" x="274" y="108">Setup Store</text>
    <!-- info -->
    <circle cx="433" cy="48" r="16" fill="none" stroke="#fff" stroke-width="2.5"/>
    <text x="433" y="56" fill="#fff" font-family="Georgia,serif" font-style="italic" font-weight="700" font-size="20" text-anchor="middle">i</text>
    <text class="step-label" x="433" y="94">Seamlessly trasnact</text>
    <text class="step-label" x="433" y="110">and request for</text>
    <text class="step-label" x="433" y="126">information</text>
    <!-- document -->
    <rect x="589" y="37" width="22" height="28" fill="none" stroke="#fff" stroke-width="2.5"/>
    <path d="M594 45 h12 M594 51 h12 M594 57 h8 M602 66 l14-18" stroke="#fff" stroke-width="2"/>
    <text class="step-label" x="600" y="103">Check out and sign</text>
  </svg>

  <ul class="abs bullets" style="left:56px;top:376px;width:700px">
    <li>Part 11 compliant signature and authentication</li>
    <li style="margin-top:12px">Leverages industry auditing skills to facilitate compliant and transparent transactions</li>
    <li style="margin-top:12px">Some of the best and industry vendors and software used</li>
  </ul>

  <svg class="abs benefits-tab" viewBox="0 0 250 50" aria-hidden="true"><polygon points="0,0 212,0 248,50 0,50" fill="var(--teal-dark)"/></svg>
  <div class="abs benefits-tab"><span>BENEFITS</span></div>

  <div class="abs benefits-band">
    <div class="benefit" style="left:83px;top:21px;width:300px"><svg width="18" height="18"><circle cx="9" cy="9" r="7.5" fill="none" stroke="#fff" stroke-width="1.8"/><path d="M7 5.5 l3.5 3.5 l-3.5 3.5" stroke="#fff" stroke-width="1.8" fill="none"/></svg>Reduce write-offs by selling excess and obsolete materials, equipment, spare parts, etc.</div>
    <div class="benefit" style="left:83px;top:81px;width:230px"><svg width="18" height="18"><circle cx="9" cy="9" r="7.5" fill="none" stroke="#fff" stroke-width="1.8"/><path d="M7 5.5 l3.5 3.5 l-3.5 3.5" stroke="#fff" stroke-width="1.8" fill="none"/></svg>Buy quality materials at a reduced price.</div>
    <div class="benefit" style="left:83px;top:126px;width:320px"><svg width="18" height="18" style="top:-8px"><circle cx="9" cy="9" r="7.5" fill="none" stroke="#fff" stroke-width="1.8"/><path d="M7 5.5 l3.5 3.5 l-3.5 3.5" stroke="#fff" stroke-width="1.8" fill="none"/></svg>Market materials if an original supplier</div>
    <div class="benefit" style="left:461px;top:21px;width:320px"><svg width="18" height="18"><circle cx="9" cy="9" r="7.5" fill="none" stroke="#fff" stroke-width="1.8"/><path d="M7 5.5 l3.5 3.5 l-3.5 3.5" stroke="#fff" stroke-width="1.8" fill="none"/></svg>Donate material to researchers</div>
    <div class="benefit" style="left:461px;top:56px;width:320px"><svg width="18" height="18"><circle cx="9" cy="9" r="7.5" fill="none" stroke="#fff" stroke-width="1.8"/><path d="M7 5.5 l3.5 3.5 l-3.5 3.5" stroke="#fff" stroke-width="1.8" fill="none"/></svg>Acquire donated materials</div>
    <div class="benefit" style="left:461px;top:92px;width:310px;line-height:18px"><svg width="18" height="18"><circle cx="9" cy="9" r="7.5" fill="none" stroke="#fff" stroke-width="1.8"/><path d="M7 5.5 l3.5 3.5 l-3.5 3.5" stroke="#fff" stroke-width="1.8" fill="none"/></svg>Collaborate and consort to reduce supply chain risk such as mutual aid agreements, joint supplier audits, etc.</div>
  </div>

  <h2 class="abs section-title" style="left:50px;top:706px"><span class="lead">OUR</span> <span class="rest">PROMISE</span></h2>
  <ul class="abs bullets" style="left:50px;top:746px;width:700px">
    <li>A greener, more cost-efficient, and quality driven supply chain through a collaborative life sciences marketplace</li>
  </ul>

  <div class="abs photo" role="img" aria-label="Photo of people sharing a warm moment at a traditional ceremony"></div>

  <div class="abs contact" style="top:806px"><div class="label">Visit</div><div class="value">www.telvamoreqx.com</div></div>
  <div class="abs contact" style="top:864px"><div class="label">Email</div><div class="value">info@telvamoreqx.com</div></div>
  <div class="abs contact" style="top:922px"><span class="label">Read our</span> <span class="value">white paper</span></div>

  <div class="abs about">
    <p>TELVAMORE-QX aspires to change the waste and risk paradigm in the life science industry.</p>
    <p>We strive to make companies better stewards of their dollars and our environment to transfer benefit to them...THE PATIENT</p>
  </div>
</div>
</body>
</html>
```